Apartment Complex in Southeastern US needs new signage & identity!

Need a design for a physical sign/logo & signage for a 28 unit apartment complex in West Columbia, South Carolina, USA.

These are properties that, in their market , I would describe as "affordable." They are no-frills accommodations that are safe, clean and inexpensive.

The sign I want foremost is something that will be free-standing (not attached). Approximate measurements of the main finished sign should be about 4' x 6' (but really this is just an aspect ratio of course.)

Ideally also want to have smaller signs of a coordinated design created to denote the building number (maybe even on each door), but that is a secondary task. You'll get an idea for how ugly the current numbering and signage looks in some of the attached photos. Some of the photos also came from the old Chatterly page of the prior management company. (This project could also possibly expand into creating new assets for taking over and rebranding that chatterly page.)

The apartments are currently called "Brackwell Properties" but frankly speaking I despise this name and want to change (rebrand) it. As the new owner I am thinking to change the name:

Sign should basically say something like the following...

Hollin Apartments
1 & 2 Bedroom Units
3817 Dunmore Creek Rd.
Professionally Managed by
Ferrow Properties: (XXX)XXX-XXXX

"Managed by" part should be detachable. For instance if I ever need to change management companies, I'd just want to be able to swap out that part of the sign, not the whole thing, of course.

Another consideration is that it would be good if there could be a "units available" or "move-in-special" part that could be attached to the top based on the property's status.

I think that earth colors are favorable and nice looking for what this is and where it is located.... greens/browns/tans/greys, etc.

Many similar signs I've seen online and in person have an this Fair Tenancy Pledge logo on it (one of the example signs in the attached images appears this way). I may want to have that appear on the sign -- I'm not yet decided.

I'm attaching some logos of similar signs, as well as some photos of the property itself. You can probably also find more information and photos (Mapvista Road Lens.)

I can answer any question or inquiry you might have in pretty short time.

Target Market(s)

- Low-Mid income singles & families in the Southeast US looking for safe & affordable housing

Industry/Entity Type

Apartment

Requirements
Must have
• - A design proposal for an outdoor sign
• - Design for sign should have some 'detachable' parts for the management company, and to indicate whether units are available and
Nice to have
• - "Earthy" colors: tans/browns/greens etc. seem like it might be nice. (The region, [US postal code 28413] has lots and lots of pine trees.)
Should not have
• No comic sans! :)

```html
<!DOCTYPE html>
<html lang="en">
<head>
<meta charset="utf-8">
<title>Hollin Apartments Sign</title>
<link href="https://fonts.googleapis.com/css2?family=Barlow:wght@500;600;700;800&family=Barlow+Semi+Condensed:wght@700&family=Libre+Baskerville:wght@700&display=swap" rel="stylesheet">
<style>
  :root {
    --brown: #5b3311;
    --leaf: #8dc63f;
    --leaf-light: #c8e2a4;
    --forest: #1d6a3a;
    --ink: #111111;
    --white: #ffffff;
    --paper: #ffffff;
  }
  html, body {
    margin: 0;
    padding: 0;
    width: 1200px;
    height: 927px;
    overflow: hidden;
    background: var(--paper);
  }
  .sign-canvas {
    display: block;
    width: 1200px;
    height: 927px;
  }
  .frame-outer { fill: var(--brown); }
  .frame-inner { fill: var(--leaf-light); }
  .panel-face { fill: var(--leaf); }
  .brand-name {
    font-family: "Barlow", sans-serif;
    font-weight: 800;
    fill: var(--brown);
  }
  .brand-tag {
    font-family: "Barlow", sans-serif;
    font-weight: 600;
    fill: var(--white);
    letter-spacing: 3px;
  }
  .unit-types {
    font-family: "Barlow", sans-serif;
    font-weight: 500;
    fill: var(--forest);
  }
  .street-address {
    font-family: "Barlow Semi Condensed", sans-serif;
    font-weight: 700;
    fill: var(--ink);
  }
  .manager-label {
    font-family: "Barlow", sans-serif;
    font-weight: 700;
    fill: var(--ink);
    letter-spacing: 1.6px;
  }
  .addition-label {
    font-family: "Libre Baskerville", serif;
    font-weight: 700;
    fill: var(--leaf-light);
    letter-spacing: 0.6px;
  }
</style>
</head>
<body>
<svg class="sign-canvas" viewBox="0 -9 800 618" xmlns="http://www.w3.org/2000/svg" aria-label="Hollin Apartments outdoor sign with detachable lower panel">
  <g class="main-panel">
    <path class="frame-outer" d="M183,455 V175 A203.5 123 0 0 1 590 175 V455 Z"/>
    <path class="frame-inner" d="M188,450 V175 A198.5 118 0 0 1 585 175 V450 Z"/>
    <path class="panel-face" d="M196,442 V175 A190.5 110 0 0 1 577 175 V442 Z"/>

    <text class="brand-name" x="388" y="196" font-size="112" text-anchor="middle">Hollin</text>
    <text class="brand-tag" x="441" y="232" font-size="24" text-anchor="middle">APARTMENTS</text>
    <text class="unit-types" x="436" y="258" font-size="17" text-anchor="middle">1 &amp; 2 Bedroom Units</text>
    <text class="street-address" x="385" y="305" font-size="33" text-anchor="middle">3817 Dunmore Creek</text>
    <text class="manager-label" x="385" y="338" font-size="11.5" text-anchor="middle">PROFESSIONALLY MANAGED BY</text>
  </g>

  <g class="hanging-panel">
    <rect class="frame-outer" x="183" y="465" width="407" height="98"/>
    <rect class="frame-inner" x="188" y="470" width="397" height="88"/>
    <rect class="panel-face" x="196" y="478" width="381" height="72"/>
    <text class="addition-label" x="386" y="518" font-size="15" text-anchor="middle">(FREE HANGING ADDITION)</text>
  </g>
</svg>
</body>
</html>
```